Velquora Design
Would like the design to go over the page in a way that can type over it.
We are a personal training and small group studio
Want it to be professional and classy
Updates
Project Deadline Extended
Reason: Asked for some modifications on a few designs, want to give the designers time to do this
Target Market(s)
All age groups, sports professionals as well as business professionals, families
Industry/Entity Type
Training
Requirements
Must have
- Must have Velquora Studio
Mina Tellaver
214 Barnicot Lane
Wexcombe Vale
South Australia 5173
Phone: 0438917263
Nice to have
- Professional classy fonts
Colour
Should not have
- Clip art
Balloons

```html
<!DOCTYPE html>
<html lang="en">
<head>
<meta charset="utf-8">
<title>Velquora Studio Letterhead</title>
<link href="https://fonts.googleapis.com/css2?family=Questrial&display=swap" rel="stylesheet">
<style>
  :root {
    --paper: #ffffff;
    --ink: #1f1f1f;
    --brand-blue: #1a8fd8;
    --deep-blue: #0f5fb0;
    --sky-blue: #3fb3ea;
    --accent-orange: #f07a2c;
    --sand: #f3b37a;
    --mist: #e4e6ea;
  }
  html, body {
    margin: 0;
    padding: 0;
    width: 900px;
    height: 1200px;
    overflow: hidden;
    background: var(--paper);
  }
  .letterhead {
    position: relative;
    width: 900px;
    height: 1200px;
    background: var(--paper);
    font-family: "Questrial", sans-serif;
    overflow: hidden;
  }
  .brand {
    position: absolute;
    left: 40px;
    top: 58px;
    display: flex;
    align-items: center;
    gap: 18px;
  }
  .brand-dot {
    width: 46px;
    height: 46px;
    border-radius: 50%;
    background: var(--accent-orange);
  }
  .brand-name {
    font-family: "Questrial", sans-serif;
    font-size: 50px;
    line-height: 1;
    color: var(--brand-blue);
    letter-spacing: 0.5px;
    margin: 0;
    font-weight: 400;
  }
  .contact {
    position: absolute;
    left: 613px;
    top: 36px;
    margin: 0;
    font-style: normal;
    font-size: 19px;
    line-height: 23px;
    color: var(--ink);
  }
  .contact span { display: block; }
  .header-swoosh, .footer-wave {
    position: absolute;
    left: 0;
    width: 900px;
  }
  .header-swoosh { top: 125px; height: 70px; }
  .footer-wave { bottom: 0; height: 90px; }
</style>
</head>
<body>
<main class="letterhead">
  <header>
    <div class="brand">
      <span class="brand-dot"></span>
      <h1 class="brand-name">Velquora Studio</h1>
    </div>
    <address class="contact">
      <span>Mina Tellaver</span>
      <span>214 Barnicot Lane</span>
      <span>Wexcombe Vale</span>
      <span>South Australia 5173</span>
      <span>Phone 0438917263</span>
    </address>
    <svg class="header-swoosh" viewBox="0 0 900 70" aria-hidden="true">
      <defs>
        <linearGradient id="swooshBlue" x1="0" x2="1" y1="0" y2="0">
          <stop offset="0" stop-color="var(--sky-blue)" stop-opacity="0"/>
          <stop offset="0.45" stop-color="var(--sky-blue)"/>
          <stop offset="1" stop-color="var(--brand-blue)"/>
        </linearGradient>
        <linearGradient id="leftBlue" x1="0" x2="1" y1="0" y2="0">
          <stop offset="0" stop-color="var(--deep-blue)"/>
          <stop offset="1" stop-color="var(--sky-blue)" stop-opacity="0"/>
        </linearGradient>
      </defs>
      <path d="M0 17 Q450 26 850 24 L850 27 Q450 30 0 22 Z" fill="var(--accent-orange)"/>
      <path d="M380 55 Q700 45 900 8 L900 30 Q700 52 380 56 Z" fill="url(#swooshBlue)"/>
      <path d="M0 30 Q250 48 520 54 Q250 52 0 46 Z" fill="url(#leftBlue)"/>
    </svg>
  </header>

  <svg class="footer-wave" viewBox="0 0 900 90" aria-hidden="true">
    <defs>
      <linearGradient id="waveBlue" x1="0" x2="1" y1="0" y2="0">
        <stop offset="0" stop-color="var(--deep-blue)"/>
        <stop offset="0.5" stop-color="var(--brand-blue)"/>
        <stop offset="1" stop-color="var(--sky-blue)"/>
      </linearGradient>
      <linearGradient id="waveSand" x1="0" x2="1" y1="0" y2="0">
        <stop offset="0" stop-color="var(--sand)"/>
        <stop offset="0.6" stop-color="var(--mist)"/>
        <stop offset="1" stop-color="var(--mist)"/>
      </linearGradient>
    </defs>
    <path d="M0 80 Q200 30 450 30 Q700 30 900 40 L900 90 L0 90 Z" fill="url(#waveBlue)"/>
    <path d="M30 90 Q220 50 450 50 Q700 50 870 90 Z" fill="url(#waveSand)"/>
  </svg>
</main>
</body>
</html>
```